Brookvale capital

We lend hard money loans for fixer upper homes and new constructions.Easy Financing on Fix Homes

Target Market(s)

People that need loans & money to buy a Home

Industry/Entity Type

Mortgage Lender

Font styles to use
Serif
Sans Serif

Colors
ffffff
9ccb3b

Requirements
Must have
• Catchy, modern, Clean
Nice to have
• Easy to read

```html
<!DOCTYPE html>
<html lang="en">
<head>
<meta charset="utf-8">
<title>Brookvale Capital Stationery</title>
<link href="https://fonts.googleapis.com/css2?family=Montserrat:wght@400;700;800&display=swap" rel="stylesheet">
<style>
:root{
  --bg:#a9a8ad;
  --paper:#ffffff;
  --lime:#b6d334;
  --green:#9ccb3b;
  --deep:#62ac3a;
  --ink:#2b2b2b;
  --grey:#666666;
}
*{margin:0;padding:0;box-sizing:border-box}
html,body{width:1200px;height:1041px;overflow:hidden}
body{background:var(--bg);font-family:Montserrat,Arial,sans-serif;position:relative}
.piece{position:absolute;background:var(--paper);overflow:hidden;box-shadow:0 1px 3px rgba(0,0,0,.25)}
.piece svg.wave{position:absolute;left:0;top:0}
.brand{position:absolute;color:var(--ink);font-weight:800;text-align:center;line-height:1}
.brand .sub{display:block;letter-spacing:.55em;margin-top:2px}
.small{position:absolute;color:var(--grey);font-weight:400;white-space:nowrap}
.small b{color:var(--deep);font-weight:700}
.folder{left:166px;top:76px;width:417px;height:541px;border-radius:3px}
.letterhead{left:615px;top:95px;width:403px;height:522px}
.env-front{left:132px;top:645px;width:451px;height:196px}
.env-back{left:615px;top:645px;width:451px;height:196px}
.card-front{left:418px;top:870px;width:166px;height:96px;border-radius:6px}
.card-back{left:615px;top:870px;width:166px;height:96px;border-radius:6px}
.rule{position:absolute;width:1px;background:var(--green)}
</style>
</head>
<body>
<svg width="0" height="0" style="position:absolute">
  <defs>
    <linearGradient id="greenFade" x1="0" x2="1" y1="0" y2="0">
      <stop offset="0" stop-color="#b6d334"/><stop offset="1" stop-color="#62ac3a"/>
    </linearGradient>
    <linearGradient id="greenFadeRev" x1="0" x2="1" y1="0" y2="0">
      <stop offset="0" stop-color="#62ac3a"/><stop offset="1" stop-color="#b6d334"/>
    </linearGradient>
  </defs>
</svg>

<!-- Presentation folder -->
<div class="piece folder">
  <svg class="wave" width="417" height="541" viewBox="0 0 417 541">
    <path d="M0 0H417V226C330 210 270 185 200 180C120 172 60 185 0 180Z" fill="url(#greenFade)"/>
    <path d="M0 175C70 160 140 160 200 170" stroke="#d3e98a" stroke-width="2" fill="none"/>
    <circle cx="206" cy="188" r="80" fill="#ffffff"/>
  </svg>
  <div class="brand" style="left:0;width:417px;top:258px;font-size:34px">Brookvale<span class="sub" style="font-size:14px">CAPITAL</span></div>
  <div class="small" style="left:0;width:417px;text-align:center;top:498px;font-size:8px">www.<b>brookvalecapital</b>.com</div>
</div>

<!-- Letterhead -->
<div class="piece letterhead">
  <svg class="wave" width="403" height="522" viewBox="0 0 403 522">
    <path d="M0 0H403V78C330 50 250 28 150 32C90 34 40 45 0 50Z" fill="url(#greenFade)"/>
    <path d="M0 44C60 30 140 22 220 26" stroke="#d3e98a" stroke-width="1.5" fill="none"/>
    <circle cx="71" cy="53" r="31" fill="#ffffff"/>
  </svg>
  <div class="brand" style="left:21px;width:100px;top:86px;font-size:14px">Brookvale<span class="sub" style="font-size:6px">CAPITAL</span></div>
  <div class="small" style="left:36px;top:492px;font-size:5px;line-height:7px">48 Harbor Lane, Fairview, NY 10990<br>212 Elm Court, Riverton, NY 10412</div>
  <div class="rule" style="left:155px;top:493px;height:12px"></div>
  <div class="small" style="left:168px;top:492px;font-size:5px;line-height:7px"><b>T:</b> (555) 014-2290<br><b>E:</b> info@brookvalecapital.com</div>
  <div class="small" style="left:297px;top:499px;font-size:5px">www.<b>brookvalecapital</b>.com</div>
</div>

<!-- Envelope front -->
<div class="piece env-front">
  <svg class="wave" width="451" height="196" viewBox="0 0 451 196">
    <path d="M0 0H451V88C370 60 290 36 190 36C110 36 50 45 0 52Z" fill="url(#greenFade)"/>
    <path d="M0 46C70 32 150 26 240 30" stroke="#d3e98a" stroke-width="1.5" fill="none"/>
    <circle cx="71" cy="56" r="30" fill="#ffffff"/>
  </svg>
  <div class="brand" style="left:21px;width:100px;top:86px;font-size:14px">Brookvale<span class="sub" style="font-size:6px">CAPITAL</span></div>
  <div class="rule" style="left:34px;top:172px;height:13px"></div>
  <div class="small" style="left:40px;top:172px;font-size:5px;line-height:7px">212 Elm Court<br>Riverton, NY 10412</div>
</div>

<!-- Envelope back -->
<div class="piece env-back">
  <svg class="wave" width="451" height="196" viewBox="0 0 451 196">
    <path d="M0 0H451L433 64H19Z" fill="url(#greenFadeRev)"/>
    <circle cx="226" cy="34" r="15" fill="none" stroke="#ffffff" stroke-width="1.5"/>
  </svg>
</div>

<!-- Business card front -->
<div class="piece card-front">
  <svg class="wave" width="166" height="96" viewBox="0 0 166 96">
    <path d="M0 0H166V45C130 30 90 18 50 18C30 18 12 21 0 24Z" fill="url(#greenFade)"/>
    <circle cx="124" cy="44" r="23" fill="#ffffff"/>
  </svg>
  <div class="brand" style="left:89px;width:70px;top:69px;font-size:10px">Brookvale<span class="sub" style="font-size:4px">CAPITAL</span></div>
  <div class="small" style="left:12px;top:36px;font-size:5px;line-height:6px"><b>JORDAN ELLIS</b><br>General Manager</div>
  <div class="small" style="left:12px;top:59px;font-size:3.6px;line-height:5px"><b>T:</b> (555) 014-2290<br><b>E:</b> info@brookvalecapital.com<br>www.<b>brookvalecapital</b>.com</div>
  <div class="small" style="left:12px;top:81px;font-size:3.6px">48 Harbor Lane, Fairview, NY 10990</div>
</div>

<!-- Business card back -->
<div class="piece card-back">
  <svg class="wave" width="166" height="96" viewBox="0 0 166 96">
    <path d="M0 0H166V62C130 46 100 42 83 42C50 42 20 52 0 56Z" fill="url(#greenFade)"/>
    <circle cx="83" cy="38" r="24" fill="#ffffff"/>
  </svg>
  <div class="brand" style="left:33px;width:100px;top:64px;font-size:11px">Brookvale<span class="sub" style="font-size:4.5px">CAPITAL</span></div>
</div>
</body>
</html>
```